Flyer-Design für Verkauf von Designerkleidung
Ich bin mehr als zufrieden, danke für den tollen Flyer, die schnelle Umsetzung und die unkomplizierten Änderungen. 5⭐️
Zielgruppe
Ich verkaufe für Privatpersonen deren gebrauchte Designerkleidung auf verschiedenen Plattformen. Die Zielgruppe ist 40 - 70 Jahre alt.
Aufgabenstellung
-eventuell Text kürzen, Zusammenfassen, übersichtlicher, ansprechender
-ein Flyer mit Vorder- und Rückseite

```html
<!DOCTYPE html>
<html lang="de">
<head>
<meta charset="utf-8">
<title>Flyer – Designerkleidung verkaufen lassen</title>
<link rel="stylesheet" href="https://fonts.googleapis.com/css2?family=Bebas+Neue&family=Oswald:wght@300;400&family=Mulish:wght@600&display=swap">
<style>
  :root {
    --backdrop: #dccbc8;
    --paper: #ffffff;
    --wine: #8b2a4a;
    --ink: #2e2428;
    --sketch-beige: #e9ddd0;
    --sketch-brown: #7a5a44;
  }
  * { box-sizing: border-box; margin: 0; padding: 0; }
  html, body {
    width: 1200px; height: 1200px; overflow: hidden;
    background: var(--backdrop);
  }
  .stage { position: relative; width: 1200px; height: 1200px; }
  .card {
    position: absolute; left: 289px; width: 652px; height: 470px;
    background: var(--paper); overflow: hidden;
  }
  .card--front { top: 101px; }
  .card--back { top: 614px; }

  /* front */
  .hero-art {
    position: absolute; left: 38px; top: 15px; width: 580px; height: 320px;
    background:
      radial-gradient(ellipse 30% 45% at 18% 55%, rgba(111,166,216,.85), transparent 70%),
      radial-gradient(ellipse 25% 40% at 42% 45%, rgba(238,138,60,.85), transparent 70%),
      radial-gradient(ellipse 25% 40% at 58% 40%, rgba(200,68,58,.85), transparent 70%),
      radial-gradient(ellipse 22% 40% at 78% 55%, rgba(111,166,216,.7), transparent 70%),
      radial-gradient(ellipse 18% 35% at 90% 40%, rgba(138,79,154,.75), transparent 70%),
      linear-gradient(180deg, #f4f1f6 0%, #ffffff 100%);
  }
  .teaser {
    position: absolute; left: 196px; top: 150px; width: 290px;
    transform: rotate(21deg);
    background: rgba(255,255,255,.55);
    padding: 6px 0 8px;
    font-family: "Mulish", sans-serif; font-weight: 600;
    font-size: 31px; line-height: 1.05; color: var(--wine);
    text-align: center;
  }
  .brand {
    position: absolute; display: flex; align-items: center; gap: 5px;
    font-family: "Oswald", sans-serif; font-weight: 400;
    color: var(--wine); white-space: nowrap;
  }
  .brand__dot { width: 7px; height: 7px; border-radius: 50%; background: var(--wine); }
  .card--front .brand { left: 500px; top: 341px; font-size: 11px; }

  .headline {
    position: absolute; left: 0; width: 100%; text-align: center;
    font-family: "Bebas Neue", sans-serif; color: var(--wine);
    font-size: 40px; line-height: 38px; letter-spacing: 1.5px;
  }
  .headline--one { top: 346px; left: -8px; }
  .headline--two { top: 383px; }
  .subline {
    position: absolute; top: 425px; left: 0; width: 100%; text-align: center;
    font-family: "Oswald", sans-serif; font-weight: 300;
    font-size: 24px; color: var(--wine); letter-spacing: .3px;
  }

  /* back */
  .runway-art {
    position: absolute; left: 3px; top: 0; width: 646px; height: 91px;
    background: linear-gradient(90deg,
      var(--sketch-beige), #c9a56a 12%, var(--sketch-brown) 22%, var(--sketch-beige) 32%,
      #4a3a4c 44%, var(--sketch-beige) 54%, #c9a56a 66%, var(--sketch-brown) 76%,
      var(--sketch-beige) 88%, #4a3a4c);
    opacity: .55;
  }
  .section-title {
    position: absolute; left: 31px; top: 123px;
    font-family: "Bebas Neue", sans-serif; font-size: 26px;
    color: var(--wine); letter-spacing: 1.5px;
  }
  .checklist { position: absolute; left: 25px; top: 156px; list-style: none; }
  .checklist li {
    position: relative; padding-left: 32px; margin-bottom: 7px;
    font-family: "Oswald", sans-serif; font-weight: 300;
    font-size: 16px; line-height: 23px; letter-spacing: 1px;
    color: var(--ink); text-transform: uppercase;
  }
  .checklist svg { position: absolute; left: 0; top: 2px; width: 28px; height: 24px; }
  .fee {
    position: absolute; left: 57px; top: 356px;
    font-family: "Oswald", sans-serif; font-weight: 300;
    font-size: 8px; line-height: 11px; text-transform: uppercase; color: var(--ink);
  }
  .fee__label { color: var(--wine); }
  .profile {
    position: absolute; left: 424px; top: 130px; width: 187px;
    font-family: "Oswald", sans-serif; font-weight: 300;
    font-size: 10.2px; line-height: 14.3px; text-transform: uppercase;
    color: var(--ink); text-align: justify; hyphens: auto;
  }
  .profile__title { font-weight: 400; color: var(--wine); font-size: 10.5px; }
  .card--back .brand { left: 23px; width: 100%; justify-content: center; top: 396px; font-size: 12px; }
  .contact {
    position: absolute; left: 24px; width: 100%; top: 425px; text-align: center;
    font-family: "Oswald", sans-serif; font-weight: 300;
    font-size: 10.5px; line-height: 15px; text-transform: uppercase; color: var(--ink);
  }
  .contact__line { display: flex; justify-content: center; align-items: center; gap: 6px; }
  .contact__icon { color: var(--wine); font-weight: 400; font-size: 12px; }
</style>
</head>
<body>
<main class="stage">

  <section class="card card--front">
    <div class="hero-art" role="img" aria-label="Aquarell-Illustration: Kleiderstange mit bunten Kleidern, zwei Kleiderpuppen mit Hut, Handtasche und Schuhe"></div>
    <p class="teaser">Zu viel Kleidung<br>im Schrank?</p>
    <div class="brand"><span class="brand__dot"></span>Marlenesorvik</div>
    <h1 class="headline headline--one">Ich verkaufe Ihre</h1>
    <h1 class="headline headline--two">Designer- und Markenkleidung für Sie!</h1>
    <p class="subline">SIE MÜSSEN NICHTS TUN - NUR AUSSORTIEREN</p>
  </section>

  <section class="card card--back">
    <div class="runway-art" role="img" aria-label="Illustration: Reihe gezeichneter Models in Modeoutfits auf dem Laufsteg"></div>

    <h2 class="section-title">Sie sortieren aus -</h2>
    <ul class="checklist">
      <li><svg viewBox="0 0 28 24"><path d="M2 13 L10 22 L27 2 L10 16 Z" fill="var(--wine)"/></svg>Ich schätze anhand von Marke,<br>Material und Zustand den Wert</li>
      <li><svg viewBox="0 0 28 24"><path d="M2 13 L10 22 L27 2 L10 16 Z" fill="var(--wine)"/></svg>Ich stelle sie auf mehreren Plattformen ein</li>
      <li><svg viewBox="0 0 28 24"><path d="M2 13 L10 22 L27 2 L10 16 Z" fill="var(--wine)"/></svg>Ich vermesse auf Wunsch und<br>verhandle den Preis mit dem Käufer</li>
      <li><svg viewBox="0 0 28 24"><path d="M2 13 L10 22 L27 2 L10 16 Z" fill="var(--wine)"/></svg>Die Käufer zahlen im Voraus</li>
      <li><svg viewBox="0 0 28 24"><path d="M2 13 L10 22 L27 2 L10 16 Z" fill="var(--wine)"/></svg>Anschliessend versende ich den Artikel</li>
    </ul>
    <p class="fee"><span class="fee__label">Meine Provision:</span><br>Meine Provision beträgt 50%. Bei höherpreisigen Kleidungsstücken<br>oder Handtaschen nennen Sie mir gerne Ihre Preisvorstellung</p>

    <div class="profile">
      <p class="profile__title">Mein Profil:</p>
      <p>Mein Name ist Marlene Sorvik, bin 32 Jahre alt, komme aus Lindenau und verkaufe schon seit vielen Jahren Markenkleidung im Internet. In Summe habe ich weit mehr als 600 positive Bewertungen auf mehreren Plattformen. Ich liebe Designerkleidung und kenne mich sehr gut mit Marken, Materialien und dem Wert der Kleidung aus. Dadurch kann ich preislich das Beste aushandeln, was möglich ist.<br>Ich dokumentiere jeden Verkauf ganz genau und Sie können auf Wunsch natürlich auch jederzeit Einblick in die Gesprächsverläufe nehmen.</p>
    </div>

    <div class="brand"><span class="brand__dot"></span>Marlenesorvik</div>

    <div class="contact">
      <p>Ich freue mich über Ihre Anfrage</p>
      <p class="contact__line">
        <svg width="12" height="10" viewBox="0 0 12 10" aria-hidden="true"><path d="M1 3 Q6 -1 11 3 L9 4.5 L8 3 Q6 2.4 4 3 L3 4.5 Z M3 5 H9 L10.5 9.5 H1.5 Z" fill="var(--wine)"/></svg>
        <span>0160 4417 382</span>
        <span class="contact__icon">@</span>
        <span>marlenesorvik@postfach-mail.de</span>
      </p>
    </div>
  </section>

</main>
</body>
</html>
```